drafting business needs a 2 sided rack card design. Size specificaton

Document Trim Size:
Full Bleed Size (starting document size)
3.86" x 8.39"
When trimmed the Rack cards are 3.74" x 8.27".
300 DPI

I need my logo, product info, and 2 pictures included

This is product information that i need:

- Floor Plans measured to QERT & PLUX standards
- Stunning HD Photography
- Vexolith - your space delivered in perfect 3D
- E &O insured
- Our products delivered next by before 10:00 AM

It also has to my my special offer: Save 50% off Vexolith, Floor Plans, and Photography

My contact info is
www.quillfenstudio.com
dorian@quillfenstudio.com
778-514-0962
Updates

Hey designers, the common element I see in most of the designs that I actually don't like is the use of orange and blue. I think there was some miscommunication. Please Don't use these colors. It really makes the designs Look cheap. I want a clean, high end look.

Target Market(s)

realtors

Industry/Entity Type

Real Estate

Font styles to use
Serif

Colors

Designer to choose colors to be used in the design.

Requirements
Must have
• At least 2 photos and my logo included. it must include all my wording with discount in bold, but classy.
Nice to have
• I want clean classy design. My logo is and 2 photos should be in design. I design should match my logo colors, I think. I have tons of other photos if you think these arent very useful
• Also I have attached a logo from vexolith. Please include this, but smaller than the Quillfen Studio. The Vexolith is just equiptment that I use
Should not have
• This is a discount promotion, but I dont want it to look cheap whatsoever

```html
<!DOCTYPE html>
<html lang="en">
<head>
<meta charset="utf-8">
<title>Quillfen Studio – Rack Cards</title>
<link rel="stylesheet" href="https://fonts.googleapis.com/css2?family=Libre+Baskerville&family=Montserrat:wght@500;600;700&family=Open+Sans:wght@400&family=Oswald:wght@600&family=Raleway:wght@300;500&display=swap">
<style>
  :root{
    --primary:#26353f;
    --primary-dark:#1b262e;
    --accent:#a8875a;
    --ribbon:#5d6d63;
    --ribbon-dark:#3f4b44;
    --ink:#333a40;
    --paper:#ffffff;
    --soft:#f4f5f6;
    --backdrop:#e6e3df;
  }
  *{box-sizing:border-box;margin:0;padding:0}
  html,body{width:1200px;height:1200px;overflow:hidden}
  body{background:var(--backdrop);position:relative;font-family:"Open Sans",sans-serif;color:var(--ink)}
  .rack-card{position:absolute;top:96px;width:456px;height:1008px;background:linear-gradient(#fff 0%,#fff 55%,var(--soft) 75%,#fff 100%);overflow:hidden;box-shadow:0 6px 18px rgba(0,0,0,.25)}
  .rack-card--front{left:108px}
  .rack-card--back{left:636px}
  .card-shapes{position:absolute;inset:0;width:456px;height:1008px}
  .brand{position:absolute;left:0;width:456px;text-align:center}
  .brand__mark{display:block;margin:0 auto;border-radius:50%;background:var(--primary)}
  .brand__name{display:block;font-family:"Libre Baskerville",serif;color:var(--primary);white-space:nowrap}
  .photo{position:absolute}
  .headline{position:absolute;left:0;width:456px;text-align:center;font-family:"Montserrat",sans-serif;white-space:nowrap}
  .headline--main{top:566px;font-size:40px;line-height:46px;font-weight:700;color:var(--primary)}
  .headline--sub{top:614px;font-size:26px;line-height:30px;font-weight:700;color:var(--accent)}
  .headline--tag{top:643px;font-size:19px;line-height:24px;font-weight:600;color:var(--ink)}
  .info-box{position:absolute;left:42px;top:706px;width:372px;height:196px;border:2px solid var(--ink);border-radius:16px}
  .info-box__title{position:absolute;left:50%;top:-14px;transform:translateX(-50%);background:#fff;padding:0 6px;font-family:"Montserrat",sans-serif;font-weight:700;font-size:19px;color:var(--primary);white-space:nowrap}
  .info-list{list-style:none;position:absolute;left:-12px;top:18px}
  .info-list li{display:flex;align-items:center;height:33.5px;font-size:13px;letter-spacing:-.1px;color:#3b3b3b;white-space:nowrap}
  .info-list svg{width:22px;height:22px;margin-right:8px;flex:none;background:#fff;border-radius:50%}
  .cta{position:absolute;font-family:"Montserrat",sans-serif;color:#fff;white-space:nowrap}
  .cta--call{left:24px;width:432px;top:938px;text-align:center;font-size:19px;font-weight:700}
  .cta--call svg{width:14px;height:14px;vertical-align:-1px;margin:0 2px}
  .site-url{position:absolute;left:0;width:436px;top:978px;text-align:center;font-family:"Montserrat",sans-serif;font-weight:500;font-size:14px;letter-spacing:3.4px;color:#fff}
  .offer-box{position:absolute;left:82px;top:626px;width:308px;height:216px;background:#fff;border:2px solid #8a8d90;border-radius:14px;box-shadow:0 10px 16px -8px rgba(0,0,0,.25)}
  .offer-ribbon{position:absolute;left:68px;top:630px;width:232px;height:48px}
  .offer-ribbon__label{position:absolute;left:0;top:0;width:214px;height:40px;line-height:40px;text-align:center;font-family:"Montserrat",sans-serif;font-weight:600;font-size:20px;color:#fff}
  .offer-save{position:absolute;left:108px;top:690px;width:21px;height:58px;background:var(--accent);color:#fff;font-family:"Raleway",sans-serif;font-weight:500;font-size:13px;display:flex;align-items:center;justify-content:center}
  .offer-save span{transform:rotate(-90deg);white-space:nowrap;letter-spacing:.5px}
  .offer-amount{position:absolute;left:136px;top:676px;width:244px;font-family:"Oswald",sans-serif;font-weight:600;font-size:64px;line-height:80px;color:var(--primary);letter-spacing:-1px;white-space:nowrap;overflow:hidden}
  .offer-items{position:absolute;left:84px;width:304px;text-align:center;white-space:nowrap;color:var(--ink)}
  .offer-items--light{top:762px;font-family:"Raleway",sans-serif;font-weight:300;font-size:23px}
  .offer-items--bold{top:792px;font-family:"Montserrat",sans-serif;font-weight:700;font-size:23px}
  .contact{position:absolute;left:0;width:456px;text-align:center;white-space:nowrap}
  .contact--lead{top:870px;font-family:"Montserrat",sans-serif;font-weight:600;font-size:19px;color:var(--accent)}
  .contact--phone{top:896px;font-family:"Montserrat",sans-serif;font-weight:700;font-size:25px;color:#3d4750}
  .contact--phone svg{width:17px;height:17px;vertical-align:-1px;margin-right:4px}
  .contact--mail{top:932px;font-size:14.5px;color:#3d4750}
  .contact--mail svg{width:30px;height:13px;vertical-align:-2px;margin-right:4px}
</style>
</head>
<body>

<section class="rack-card rack-card--front">
  <svg class="card-shapes" viewBox="0 0 456 1008" aria-hidden="true">
    <path d="M13,196 H368 Q382,196 388,206 H13 Z" fill="var(--accent)"/>
    <rect x="56" y="536" width="386" height="12" fill="var(--primary)"/>
    <path d="M24,972 C26,950 44,934 76,934 H456 V972 Z" fill="var(--primary)"/>
    <rect x="396" y="962" width="60" height="46" fill="var(--primary-dark)"/>
    <path d="M0,970 H396 C418,970 432,988 436,1008 H0 Z" fill="var(--accent)"/>
  </svg>

  <div class="brand" style="top:40px">
    <span class="brand__mark" style="width:90px;height:90px"></span>
    <span class="brand__name" style="font-size:32px;margin-top:8px">Quillfen Studio</span>
  </div>

  <div class="photo" role="img" aria-label="Photo of a staged bedroom with a made bed, two nightstands with lamps and a round mirror"
       style="left:13px;top:212px;width:429px;height:318px;border-radius:0 48px 0 48px;background:linear-gradient(180deg,#cfc3b8 0%,#b9aca3 45%,#8c7f79 70%,#c9b8b4 100%)"></div>

  <div class="headline headline--main">FLOOR PLANS</div>
  <div class="headline headline--sub">PROPERTY PHOTOGRAPHY</div>
  <div class="headline headline--tag">Vexolith: Real Spaces in Perfect 3D</div>

  <div class="info-box">
    <div class="info-box__title">PRODUCT INFORMATION</div>
    <ul class="info-list">
      <li><svg viewBox="0 0 22 22"><circle cx="11" cy="11" r="10" fill="none" stroke="#444" stroke-width="1.6"/><circle cx="11" cy="11" r="7" fill="#444"/><path d="M7.5,11.2 L10,13.6 L14.6,8.6" fill="none" stroke="#fff" stroke-width="1.8"/></svg>Floor Plans measured to QERT &amp;amp; PLUX standards</li>
      <li><svg viewBox="0 0 22 22"><circle cx="11" cy="11" r="10" fill="none" stroke="#444" stroke-width="1.6"/><circle cx="11" cy="11" r="7" fill="#444"/><path d="M7.5,11.2 L10,13.6 L14.6,8.6" fill="none" stroke="#fff" stroke-width="1.8"/></svg>Stunning HD Photography</li>
      <li><svg viewBox="0 0 22 22"><circle cx="11" cy="11" r="10" fill="none" stroke="#444" stroke-width="1.6"/><circle cx="11" cy="11" r="7" fill="#444"/><path d="M7.5,11.2 L10,13.6 L14.6,8.6" fill="none" stroke="#fff" stroke-width="1.8"/></svg>Vexolith - your space delivered in perfect 3D</li>
      <li><svg viewBox="0 0 22 22"><circle cx="11" cy="11" r="10" fill="none" stroke="#444" stroke-width="1.6"/><circle cx="11" cy="11" r="7" fill="#444"/><path d="M7.5,11.2 L10,13.6 L14.6,8.6" fill="none" stroke="#fff" stroke-width="1.8"/></svg>E &amp;O insured</li>
      <li><svg viewBox="0 0 22 22"><circle cx="11" cy="11" r="10" fill="none" stroke="#444" stroke-width="1.6"/><circle cx="11" cy="11" r="7" fill="#444"/><path d="M7.5,11.2 L10,13.6 L14.6,8.6" fill="none" stroke="#fff" stroke-width="1.8"/></svg>Our products delivered next by before 10:00 AM</li>
    </ul>
  </div>

  <div class="cta cta--call">Call Us <svg viewBox="0 0 24 24"><path d="M6.6,10.8 C8,13.6 10.4,16 13.2,17.4 L15.4,15.2 C15.7,14.9 16.1,14.8 16.4,15 C17.5,15.4 18.7,15.6 20,15.6 C20.6,15.6 21,16 21,16.6 V20 C21,20.6 20.6,21 20,21 C10.6,21 3,13.4 3,4 C3,3.4 3.4,3 4,3 H7.5 C8.1,3 8.5,3.4 8.5,4 C8.5,5.3 8.7,6.5 9.1,7.6 C9.2,7.9 9.1,8.3 8.9,8.6 Z" fill="#fff"/></svg> 778-514-0962</div>
  <div class="site-url">WWW.QUILLFENSTUDIO.COM</div>
</section>

<section class="rack-card rack-card--back">
  <svg class="card-shapes" viewBox="0 0 456 1008" aria-hidden="true">
    <rect x="0" y="9" width="456" height="11" fill="var(--accent)"/>
    <rect x="0" y="9" width="10" height="500" fill="var(--accent)"/>
    <rect x="56" y="570" width="400" height="12" fill="var(--primary)"/>
    <path d="M52,972 C56,964 64,962 76,962 H456 V972 Z" fill="var(--primary)"/>
    <rect x="396" y="962" width="60" height="46" fill="var(--primary-dark)"/>
    <path d="M0,970 H396 C418,970 432,988 436,1008 H0 Z" fill="var(--accent)"/>
  </svg>

  <div class="brand" style="top:92px">
    <span class="brand__mark" style="width:80px;height:80px"></span>
    <span class="brand__name" style="font-size:29px;margin-top:8px">Quillfen Studio</span>
  </div>

  <div class="photo" role="img" aria-label="Photo of a bright living room with large windows, a white sofa, a rug on a wood floor and a stone fireplace"
       style="left:16px;top:268px;width:440px;height:298px;border-radius:0 0 0 48px;background:linear-gradient(180deg,#f2f3f2 0%,#d9dbd8 40%,#a59b8c 70%,#5e4636 100%)"></div>

  <div class="offer-box"></div>
  <svg class="offer-ribbon" viewBox="0 0 232 48" aria-hidden="true">
    <path d="M0,40 L0,48 L12,40 Z" fill="var(--ribbon-dark)"/>
    <path d="M0,0 H214 L232,20 L214,40 H0 Z" fill="var(--ribbon)"/>
  </svg>
  <div class="offer-ribbon"><div class="offer-ribbon__label">SPECIAL OFFER:</div></div>
  <div class="offer-save"><span>SAVE</span></div>
  <div class="offer-amount">50% OFF</div>
  <div class="offer-items offer-items--light">Vexolith, Floor Plans,</div>
  <div class="offer-items offer-items--bold">AND PHOTOGRAPHY</div>

  <div class="contact contact--lead">For more details Contact Us</div>
  <div class="contact contact--phone"><svg viewBox="0 0 24 24"><path d="M6.6,10.8 C8,13.6 10.4,16 13.2,17.4 L15.4,15.2 C15.7,14.9 16.1,14.8 16.4,15 C17.5,15.4 18.7,15.6 20,15.6 C20.6,15.6 21,16 21,16.6 V20 C21,20.6 20.6,21 20,21 C10.6,21 3,13.4 3,4 C3,3.4 3.4,3 4,3 H7.5 C8.1,3 8.5,3.4 8.5,4 C8.5,5.3 8.7,6.5 9.1,7.6 C9.2,7.9 9.1,8.3 8.9,8.6 Z" fill="var(--primary)"/></svg>778-514-0962</div>
  <div class="contact contact--mail"><svg viewBox="0 0 30 13"><path d="M0,4 H8 M2,7 H8 M4,10 H8" stroke="var(--primary)" stroke-width="1.2"/><rect x="10.5" y="1" width="18" height="11" rx="1" fill="none" stroke="var(--primary)" stroke-width="1.2"/><path d="M10.5,1.5 L19.5,8 L28.5,1.5" fill="none" stroke="var(--primary)" stroke-width="1.2"/></svg>dorian@quillfenstudio.com</div>
  <div class="site-url">WWW.QUILLFENSTUDIO.COM</div>
</section>

</body>
</html>
```